Half-fold brochure for Birch Glow & Laser membership

We would like a professional designer to help us with designing a half-fold brochure for our membership program. Attached to this project is the draft brochure to showcase the content and typical color scheme. Please take a moment to visit oue website and Instagram to get an idea of what our brand is about.

www.BirchGlowLaser.example
www.Instagram.com/BirchGlowLaser

Target Market(s)

25 - 45 female working professional

Industry/Entity Type

Beauty

Font styles to use
Other font styles liked:
• Josefin Sans, Lato

Colors

Designer to choose colors to be used in the design.

Requirements
Must have
• Logo, color scheme, website, instagram address, facebook address, pictures
Nice to have
• Mobile app mock-up
Should not have
• models outside of 25 - 45 age range

```html
<!DOCTYPE html>
<html lang="en">
<head>
<meta charset="utf-8">
<title>Birch Glow &amp; Laser — Membership Brochure Inside Spread</title>
<link rel="stylesheet" href="https://fonts.googleapis.com/css2?family=Josefin+Sans:wght@400;600;700&family=Lato:wght@400;700;900&display=swap">
<style>
  :root {
    --orange: #f0a02a;
    --orange-deep: #e9931c;
    --sage: #9cbfa5;
    --sage-deep: #86ad92;
    --ink: #141414;
    --grey-text: #5a5a5a;
    --paper: #f6f5f3;
    --blush: #f1e6df;
    --blush-soft: #f5ece6;
    --coral-line: #ef9f8a;
    --backdrop: #d9d8dc;
  }
  * { box-sizing: border-box; margin: 0; padding: 0; }
  html, body { width: 1200px; height: 840px; overflow: hidden; }
  body {
    background: var(--backdrop);
    font-family: "Lato", sans-serif;
    color: var(--ink);
    position: relative;
  }
  .spread {
    position: absolute;
    left: 40px; top: 25px;
    width: 1120px; height: 790px;
    display: flex;
    box-shadow: 0 10px 30px rgba(0,0,0,.15);
  }
  .page {
    position: relative;
    width: 560px; height: 790px;
    background: var(--paper);
    overflow: hidden;
  }
  .page--left { border-right: 1px solid #e4e1de; }

  /* shared headings */
  .page-title {
    position: absolute;
    font-family: "Josefin Sans", sans-serif;
    font-weight: 700;
    font-size: 34px;
    letter-spacing: .5px;
    line-height: 1;
    text-transform: uppercase;
  }
  .page-title .accent { color: var(--orange); }
  .page-subtitle {
    position: absolute;
    font-family: "Josefin Sans", sans-serif;
    font-size: 16px;
  }
  .section-label {
    position: absolute;
    left: 40px;
    font-family: "Josefin Sans", sans-serif;
    font-weight: 700;
    font-size: 17px;
    letter-spacing: .5px;
    text-transform: uppercase;
  }
  .photo { position: absolute; }

  /* left page */
  .corner-blob { position: absolute; left: 0; top: 0; }
  .rewards-title { left: 40px; top: 58px; }
  .rewards-subtitle { left: 42px; top: 98px; }
  .label-vouchers { top: 140px; }
  .label-services { top: 310px; }

  .ticket-row {
    position: absolute;
    left: 40px;
    display: flex;
    gap: 14px;
  }
  .ticket-row--vouchers { top: 170px; }
  .ticket-row--services { top: 340px; }
  .ticket { display: flex; width: 128px; height: 112px; }
  .ticket__stub {
    width: 26px;
    background: var(--sage);
    -webkit-mask: radial-gradient(circle at 0 50%, transparent 3.5px, #000 4px) 0 0 / 100% 9px repeat-y;
            mask: radial-gradient(circle at 0 50%, transparent 3.5px, #000 4px) 0 0 / 100% 9px repeat-y;
  }
  .ticket__face {
    flex: 1;
    background: var(--orange);
    color: #fff;
    display: flex;
    flex-direction: column;
    justify-content: center;
    padding-left: 14px;
    font-family: "Josefin Sans", sans-serif;
  }
  .ticket__amount { font-weight: 700; font-size: 32px; line-height: 1; }
  .ticket__service {
    font-weight: 700; font-size: 13px; line-height: 1.15;
    text-transform: uppercase; letter-spacing: .3px;
  }
  .ticket__kind { font-size: 17px; margin-top: 4px; }

  .photo--treatment { right: 0; top: 150px; }
  .photo--facial { left: 0; bottom: 0; }

  /* right page */
  .wave-top, .wave-bottom { position: absolute; left: 0; }
  .wave-top { top: 0; }
  .wave-bottom { bottom: 0; }
  .photo--portrait { right: 0; top: 60px; }
  .perks-title { left: 40px; top: 118px; }
  .perks-subtitle { left: 40px; top: 160px; }

  .perk-card {
    position: absolute;
    width: 215px; height: 150px;
    border: 2px solid var(--orange);
    border-radius: 36px 70px 40px 60px;
    box-shadow: 4px 5px 8px rgba(0,0,0,.08);
    display: flex;
    align-items: center;
    padding: 18px 22px 0 30px;
  }
  .perk-card--sage { border-color: var(--sage); }
  .perk-card__number {
    position: absolute;
    top: -30px; left: 10px;
    font-family: "Josefin Sans", sans-serif;
    font-weight: 700;
    font-size: 66px;
    line-height: 1;
    color: var(--orange);
    background: var(--paper);
    padding: 0 4px;
  }
  .perk-card--sage .perk-card__number { color: var(--sage); }
  .perk-card__text {
    font-family: "Josefin Sans", sans-serif;
    font-weight: 700;
    font-size: 15px;
    line-height: 1.1;
    color: var(--grey-text);
    text-transform: uppercase;
    letter-spacing: .6px;
  }
  .perk-card__text .accent { color: var(--orange); }
  .perk-1 { left: 45px;  top: 250px; }
  .perk-2 { left: 305px; top: 330px; }
  .perk-3 { left: 45px;  top: 450px; }
  .perk-4 { left: 305px; top: 530px; }

  .website {
    position: absolute;
    left: 0; right: 0; bottom: 42px;
    text-align: center;
    font-family: "Josefin Sans", sans-serif;
    font-size: 17px;
    letter-spacing: .3px;
  }
</style>
</head>
<body>
<main class="spread">

  <section class="page page--left">
    <svg class="corner-blob" width="260" height="180" viewBox="0 0 260 180" aria-hidden="true">
      <path d="M0 0 H200 C170 40 120 60 90 110 C70 150 30 170 0 175 Z" fill="var(--blush-soft)"/>
    </svg>

    <h1 class="page-title rewards-title">Glowpoint <span class="accent">Rewards</span></h1>
    <p class="page-subtitle rewards-subtitle">All members earn 1 point per $1 spent.</p>

    <h2 class="section-label label-vouchers">Redeem points for vouchers.</h2>
    <div class="ticket-row ticket-row--vouchers">
      <div class="ticket"><div class="ticket__stub"></div><div class="ticket__face"><span class="ticket__amount">$5</span><span class="ticket__kind">Voucher</span></div></div>
      <div class="ticket"><div class="ticket__stub"></div><div class="ticket__face"><span class="ticket__amount">$10</span><span class="ticket__kind">Voucher</span></div></div>
      <div class="ticket"><div class="ticket__stub"></div><div class="ticket__face"><span class="ticket__amount">$50</span><span class="ticket__kind">Voucher</span></div></div>
    </div>

    <h2 class="section-label label-services">Redeem points for free services.</h2>
    <div class="ticket-row ticket-row--services">
      <div class="ticket"><div class="ticket__stub"></div><div class="ticket__face"><span class="ticket__service">Laser Hair<br>Removal</span><span class="ticket__kind">Voucher</span></div></div>
      <div class="ticket"><div class="ticket__stub"></div><div class="ticket__face"><span class="ticket__service">IPL<br>Facial</span><span class="ticket__kind">Voucher</span></div></div>
      <div class="ticket"><div class="ticket__stub"></div><div class="ticket__face"><span class="ticket__service">Chemical<br>Peel</span><span class="ticket__kind">Voucher</span></div></div>
    </div>

    <svg class="photo photo--treatment" width="120" height="330" viewBox="0 0 120 330" role="img" aria-label="Photo of a gloved practitioner performing a laser treatment">
      <defs>
        <linearGradient id="treatmentTone" x1="0" y1="0" x2="1" y2="1">
          <stop offset="0" stop-color="#c9c3bd"/>
          <stop offset=".55" stop-color="#6f6660"/>
          <stop offset="1" stop-color="#b98a6a"/>
        </linearGradient>
      </defs>
      <path d="M120 0 C60 10 20 60 18 140 C16 220 50 290 120 330 Z" fill="url(#treatmentTone)"/>
      <path d="M110 0 C50 14 10 64 8 140 C6 222 44 294 115 330" fill="none" stroke="var(--orange)" stroke-width="3"/>
    </svg>

    <svg class="photo photo--facial" width="560" height="320" viewBox="0 0 560 320" role="img" aria-label="Photo of a woman relaxing during a facial treatment with gloved hands">
      <defs>
        <linearGradient id="facialTone" x1="0" y1="0" x2="1" y2="1">
          <stop offset="0" stop-color="#e9e9ec"/>
          <stop offset=".45" stop-color="#e0b592"/>
          <stop offset="1" stop-color="#eef0f3"/>
        </linearGradient>
      </defs>
      <path d="M0 40 C90 -10 200 10 270 70 C330 120 380 150 460 200 C500 230 520 280 520 320 H0 Z" fill="url(#facialTone)"/>
      <path d="M0 28 C95 -22 205 -2 280 60 C340 110 395 140 475 190 C520 222 540 275 540 320" fill="none" stroke="var(--coral-line)" stroke-width="2"/>
    </svg>
  </section>

  <section class="page page--right">
    <svg class="wave-top" width="560" height="130" viewBox="0 0 560 130" aria-hidden="true">
      <path d="M0 0 H560 V40 C440 70 380 20 300 45 C220 70 150 40 80 70 C40 88 15 110 0 120 Z" fill="var(--blush-soft)"/>
    </svg>

    <svg class="photo photo--portrait" width="230" height="240" viewBox="0 0 230 240" role="img" aria-label="Photo of a woman touching her cheek, admiring smooth skin">
      <defs>
        <linearGradient id="portraitTone" x1="0" y1="0" x2="1" y2="1">
          <stop offset="0" stop-color="#cdb89e"/>
          <stop offset=".5" stop-color="#6b5448"/>
          <stop offset="1" stop-color="#c9a98f"/>
        </linearGradient>
      </defs>
      <path d="M40 0 H230 V240 C180 230 140 200 110 160 C80 120 60 70 40 0 Z" fill="var(--orange)"/>
      <path d="M60 0 H230 V225 C185 215 150 190 125 150 C100 110 78 60 60 0 Z" fill="url(#portraitTone)"/>
    </svg>

    <h1 class="page-title perks-title">Other <span class="accent">Perks</span></h1>
    <p class="page-subtitle perks-subtitle">Continue benefiting from your membership.</p>

    <div class="perk-card perk-1">
      <span class="perk-card__number">1</span>
      <p class="perk-card__text"><span class="accent">10%</span> discount<br>on skin care<br>products</p>
    </div>
    <div class="perk-card perk-card--sage perk-2">
      <span class="perk-card__number">2</span>
      <p class="perk-card__text">Share<br>membership<br>with your family</p>
    </div>
    <div class="perk-card perk-card--sage perk-3">
      <span class="perk-card__number">3</span>
      <p class="perk-card__text">Access to in-<br>house monthly<br>payment plans</p>
    </div>
    <div class="perk-card perk-4">
      <span class="perk-card__number">4</span>
      <p class="perk-card__text">Exclusive<br>monthly member<br>savings</p>
    </div>

    <svg class="wave-bottom" width="560" height="150" viewBox="0 0 560 150" aria-hidden="true">
      <path d="M0 40 C90 10 170 55 260 45 C360 35 430 80 560 60 V150 H0 Z" fill="var(--blush)"/>
    </svg>
    <p class="website">www.BirchGlowLaser.example</p>
  </section>

</main>
</body>
</html>
```